UPDATE 2: I HAVE ATTACHED TWO PHOTOS; PLEASE CONSIDER USING EITHER ONE IN A NEW DESIGN. THANK YOU.
UPDATE: I HAVE INCLUDED 4 SAMPLE BOOK COVERS THAT I LIKE TO HELP YOU ORIENT YOUR DESIGN WORK
Looking for book cover, spine, and back for a MEMOIR. Details:
TITLE: Mama's Quiet Orchard
AUTHOR: Lorivel Brashton
GENRE: Memoir
STYLE REQUESTED: Abstract and colorful; designers are welcome to get creative. Note that the memoir takes place largely in a poor African American city.
BOOK SUMMARY: As a young girl, Lorivel Brashton—or “Rivvy” to her friends and family—discovers the man she thought was her father wasn’t, and her real biological father wants little if anything to do with her. What follows is the story of a girl’s longing, a longing disturbed by abuse, disappointment, and loneliness.
Set against the backdrop of Gary, Indiana—the then “murder capital of the world”—Mama’s Quiet Orchard follows Lorivel as she searches and grows, following a path that eventually leads her to self-discovery and self-confidence.
Template provided for InDesign. Please note margins and bleed areas. Make sure any letters/words are at least one inch from edges. On spine, leave three inches at bottom for publisher's logo.
Updates
To all designers: Please note that there should NOT be any images of people as part of your designs. Thank you, and my apologies for not mentioning that in the initial ask.

```html
<!DOCTYPE html>
<html lang="en">
<head>
<meta charset="utf-8">
<title>Mama's Quiet Orchard — Book Cover</title>
<link rel="stylesheet" href="https://fonts.googleapis.com/css2?family=Jost:wght@400;500&family=Bodoni+Moda:wght@400&family=Sacramento&display=swap">
<style>
  :root {
    --ink-white: #ffffff;
    --paint-red: #e0412f;
    --paint-orange: #ec7a4a;
    --paint-pink: #f07e95;
    --paint-rose: #ee4f86;
    --paint-lilac: #a994d6;
    --paint-violet: #9a72c4;
    --paint-cream: #f3dcc8;
  }
  html, body {
    margin: 0;
    padding: 0;
    width: 750px;
    height: 1200px;
    overflow: hidden;
    background: #ffffff;
  }
  .cover {
    position: relative;
    width: 750px;
    height: 1200px;
    overflow: hidden;
    color: var(--ink-white);
  }
  .cover__artwork {
    position: absolute;
    inset: 0;
    background:
      radial-gradient(ellipse 260px 380px at 60px 240px, rgba(169,148,214,0.95), rgba(169,148,214,0) 75%),
      radial-gradient(ellipse 330px 260px at 380px 170px, rgba(224,65,47,0.95), rgba(224,65,47,0) 80%),
      radial-gradient(ellipse 300px 320px at 660px 260px, rgba(236,122,74,0.9), rgba(236,122,74,0) 80%),
      radial-gradient(ellipse 320px 200px at 420px 620px, rgba(243,220,200,0.85), rgba(243,220,200,0) 80%),
      radial-gradient(ellipse 260px 260px at 700px 640px, rgba(169,148,214,0.85), rgba(169,148,214,0) 80%),
      radial-gradient(ellipse 340px 240px at 160px 760px, rgba(240,126,149,0.9), rgba(240,126,149,0) 80%),
      radial-gradient(ellipse 260px 180px at 680px 1000px, rgba(238,79,134,0.85), rgba(238,79,134,0) 80%),
      radial-gradient(ellipse 380px 240px at 360px 1080px, rgba(154,114,196,0.95), rgba(154,114,196,0) 80%),
      linear-gradient(180deg, var(--paint-orange) 0%, var(--paint-pink) 50%, var(--paint-violet) 100%);
  }
  .cover__label {
    position: absolute;
    top: 205px;
    left: 0;
    width: 100%;
    text-align: center;
    font-family: "Bodoni Moda", "Didot", serif;
    font-weight: 400;
    font-size: 72px;
    line-height: 1;
  }
  .title {
    position: absolute;
    left: 0;
    width: 100%;
    margin: 0;
    text-align: center;
    font-family: "Jost", "Futura", sans-serif;
    font-weight: 500;
    line-height: 1;
  }
  .title__top {
    top: 378px;
    font-size: 160px;
    letter-spacing: 4px;
  }
  .title__bottom {
    top: 636px;
    font-size: 132px;
    letter-spacing: 2px;
  }
  .title__middle {
    position: absolute;
    top: 540px;
    left: 0;
    width: 100%;
    height: 80px;
  }
  .title__rules {
    position: absolute;
    inset: 0;
  }
  .title__script {
    position: absolute;
    top: 0;
    left: 0;
    width: 100%;
    text-align: center;
    font-family: "Sacramento", cursive;
    font-size: 92px;
    line-height: 80px;
  }
  .divider {
    position: absolute;
    top: 886px;
    left: 238px;
    width: 274px;
    height: 2px;
    background: var(--ink-white);
  }
  .author {
    position: absolute;
    top: 930px;
    left: 0;
    width: 100%;
    text-align: center;
    font-family: "Jost", "Futura", sans-serif;
    font-weight: 400;
    font-size: 48px;
    letter-spacing: 12px;
    padding-left: 12px;
    box-sizing: border-box;
    line-height: 1;
  }
</style>
</head>
<body>
  <main class="cover">
    <div class="cover__artwork" role="img" aria-label="Abstract painted background of loose brush strokes in red, orange, pink and lilac"></div>

    <p class="cover__label">A Memoir</p>

    <h1 class="title-block" aria-label="Mama's Quiet Orchard">
      <span class="title title__top">MAMA’S</span>
      <span class="title__middle">
        <svg class="title__rules" width="750" height="80" viewBox="0 0 750 80" aria-hidden="true">
          <polygon points="113,45 258,41 258,49" fill="#ffffff"/>
          <polygon points="493,41 637,45 493,49" fill="#ffffff"/>
        </svg>
        <span class="title__script">quiet</span>
      </span>
      <span class="title title__bottom">ORCHARD</span>
    </h1>

    <div class="divider"></div>

    <p class="author">LORIVEL BRASHTON</p>
  </main>
</body>
</html>
```